4x6 -ish post card to let the neighborhood know where here.

Hi All, I opened a high end wine & spirits shop and am looking to get out some sort of a 4x6 postcard a flyer to let people know where in the area. Looking for something clean cut that can maybe incorporate a few pictures from our store on along the top and our logo. Ideally a white-ish background.

```html
<!DOCTYPE html>
<html lang="en">
<head>
<meta charset="utf-8">
<title>Harborline Wine &amp; Spirits – Postcard</title>
<link rel="stylesheet" href="https://fonts.googleapis.com/css2?family=Merriweather:wght@400;700;900&family=Oswald:wght@500;600&display=swap">
<style>
:root{
  --gold:#c4922f;
  --gold-light:#e7c884;
  --ink:#141414;
  --cream:#faf6ee;
  --paper:#ffffff;
  --page:#ffffff;
  --grey:#b9b9b9;
  --text:#2b2b2b;
  --on-gold:#fff8ea;
}
*{box-sizing:border-box;margin:0;padding:0}
html,body{width:1200px;height:2766px;overflow:hidden;background:var(--page)}
body{position:relative;font-family:"Merriweather",Georgia,serif;color:var(--text)}

.preview{position:absolute;width:972px;height:648px;transform-origin:0 0;transform:scale(.6132)}
.preview-back{left:125px;top:122px}
.preview-front{left:442px;top:397px}
.sheet-front{position:absolute;left:79px;top:1118px}
.sheet-back{position:absolute;left:79px;top:1918px}

.card{position:relative;width:972px;height:648px;overflow:hidden;box-shadow:0 4px 14px rgba(0,0,0,.25)}
.front{background:var(--cream)}
.back{background:var(--paper)}
.shapes{position:absolute;inset:0;width:100%;height:100%}

.brand{position:absolute;display:flex;align-items:center;gap:12px;color:var(--gold);font-family:"Merriweather",Georgia,serif;font-weight:700;letter-spacing:1px;line-height:1.05}
.brand-dot{width:18px;height:18px;border-radius:50%;background:var(--gold);flex:none}
.brand-name{font-size:28px}
.front .brand{left:35px;top:66px}
.back .brand{left:520px;top:56px}
.back .brand-name{font-size:24px}

.kicker{position:absolute;left:35px;top:176px;font-size:24px;font-weight:900;color:var(--gold);padding-bottom:7px;border-bottom:4px solid var(--ink);width:443px;white-space:nowrap}
.headline{position:absolute;font-family:"Oswald","Arial Narrow",sans-serif;font-weight:600;color:var(--ink);text-transform:uppercase;letter-spacing:-1px;line-height:1;white-space:nowrap}
.front .headline{left:33px;top:230px;font-size:42px}
.subtitle{position:absolute;font-weight:900;text-transform:uppercase;white-space:nowrap}
.front .subtitle{left:35px;top:285px;font-size:21px;color:var(--gold)}
.service-bar{position:absolute;left:35px;width:440px;height:26px;border-left:4px solid var(--gold);background:linear-gradient(90deg,var(--gold) 0%,var(--gold-light) 55%,rgba(231,200,132,0) 100%);font-weight:900;font-size:19px;color:var(--ink);padding-left:16px;line-height:26px;white-space:nowrap}
.bar-1{top:327px}
.bar-2{top:360px}
.intro{position:absolute;left:35px;top:408px;width:410px;font-size:16px;line-height:22px;color:var(--text)}
.address{position:absolute;left:35px;top:509px;display:flex;align-items:center;gap:10px;font-size:21px;color:var(--text);white-space:nowrap}
.address svg{width:20px;height:28px;fill:var(--gold)}
.front .web{position:absolute;left:126px;top:582px;font-size:21px;font-weight:900;color:var(--ink)}

.photo{position:absolute;border-radius:50%;overflow:hidden}
.photo-bottles{left:510px;top:-80px;width:580px;height:580px;background:radial-gradient(circle at 35% 30%,#d9a56a 0%,#8a4a22 30%,#3b1f12 60%,#1d0f08 100%)}
.photo-storefront{left:465px;top:319px;width:245px;height:245px;border:11px solid var(--ink);background:linear-gradient(160deg,#e6e6e6 0%,#b8bec4 40%,#5d6670 75%,#3a3f45 100%)}

.perks{position:absolute;right:40px;top:540px;text-align:right;color:var(--on-gold);font-weight:700;font-size:23px;line-height:35px;white-space:nowrap}
.perk-row{display:flex;align-items:center;justify-content:flex-end;gap:16px}
.perk-row svg{width:34px;height:28px;fill:var(--ink)}

.back .headline{left:33px;top:34px;font-size:32px}
.back .subtitle{left:33px;top:74px;font-size:20px;color:var(--on-gold)}
.review{position:absolute;left:33px;top:112px;width:440px;color:var(--on-gold)}
.stars{display:block;text-align:center;color:#f4c53a;font-size:30px;letter-spacing:2px;line-height:32px;margin-left:-20px}
.quote-mark{position:absolute;font-family:"Merriweather",Georgia,serif;font-weight:900;font-size:44px;color:var(--on-gold);line-height:1}
.quote-open{left:0;top:28px}
.quote-close{left:385px;top:158px}
.review-text{margin-left:32px;font-size:14.5px;line-height:19.5px}
.reviewer{margin-left:32px;margin-top:8px;font-size:15px;font-weight:700;line-height:21px}
.hours{position:absolute;left:36px;top:358px;line-height:1}
.hours-open{font-weight:900;font-size:18px;color:var(--on-gold)}
.hours-days{font-family:"Oswald","Arial Narrow",sans-serif;font-weight:600;font-size:22px;letter-spacing:-.5px;color:var(--ink);margin-top:4px;white-space:nowrap}
.photo-shelf{left:224px;top:343px;width:104px;height:104px;border:4px solid var(--ink);background:linear-gradient(150deg,#f1f1f1 0%,#9aa7c7 45%,#3a4467 100%)}
.photo-display{left:303px;top:343px;width:104px;height:104px;border:4px solid var(--ink);background:linear-gradient(150deg,#f7f4ec 0%,#cfd7df 50%,#6e7a88 100%)}
.map{position:absolute;left:33px;top:438px;width:187px;height:88px;background:linear-gradient(120deg,#b9cbe3 0%,#b9cbe3 30%,#dcdfe4 31%,#e9eaed 100%)}
.back .address{left:230px;top:462px;width:270px;font-size:21px;line-height:29px;white-space:normal;display:block}
.call{position:absolute;left:33px;top:540px;width:356px;height:35px;border-radius:18px;background:var(--ink);display:flex;align-items:center;gap:10px;padding-left:14px;color:var(--on-gold);white-space:nowrap}
.call-label{font-size:14px;font-weight:900;margin-right:4px}
.call svg{width:22px;height:22px;fill:var(--on-gold)}
.call-number{font-size:23px;font-weight:700}
.contact-row{position:absolute;left:36px;top:587px;display:flex;gap:20px;font-size:14px;font-weight:700;color:var(--ink);white-space:nowrap}
.contact-row span{display:flex;align-items:center;gap:8px}
.contact-row svg{width:18px;height:18px;fill:none;stroke:var(--on-gold);stroke-width:1.6}
.stamp{position:absolute;left:819px;top:50px;width:103px;height:114px;border:3px solid #d7d7d7;border-radius:10px}
.accept{position:absolute;left:630px;top:578px;display:flex;align-items:center;gap:10px}
.accept-label{font-size:12.5px;line-height:14px;color:#555;margin-right:2px}
.pay{width:77px;height:32px;border-radius:5px;background:var(--grey);color:#fff;font-size:12px;font-weight:700;display:flex;align-items:center;justify-content:center}
</style>
</head>
<body>

<!-- ===== Small overview pair ===== -->
<div class="preview preview-back">
  <section class="card back">
    <svg class="shapes" viewBox="0 0 972 648" aria-hidden="true">
      <path fill="var(--gold)" d="M0 0H455C515 20 548 95 543 165C538 245 485 290 480 350C476 430 560 480 610 555C632 590 645 620 652 648H0Z"/>
      <path fill="var(--ink)" d="M0 109H480C515 150 522 205 510 250C498 295 470 318 445 335H0Z"/>
    </svg>
    <div class="headline">Harborline Wine &amp; Spirits</div>
    <div class="subtitle">High End Wine &amp; Spirits Shop</div>
    <div class="review">
      <span class="stars">★★★★★</span>
      <span class="quote-mark quote-open">“</span>
      <p class="review-text">Great neighborhood liquor store. Very neat, very clean, and modern looking. The owner is very accommodating and if she doesn't have something, she's willing to try and get it for you. Prices seem to be on par with other stores in the area.<br>I'd rather shop here and support a small business instead of one of the super-mega booze stores.</p>
      <span class="quote-mark quote-close">”</span>
      <p class="reviewer">Dana R.<br>Fairhaven, CT</p>
    </div>
    <div class="hours"><div class="hours-open">OPEN ON</div><div class="hours-days">MONDAY TO SUNDAY</div></div>
    <div class="photo photo-shelf" role="img" aria-label="Photo of bottles lined up on a store shelf"></div>
    <div class="photo photo-display" role="img" aria-label="Photo of a chilled bottle display in the store"></div>
    <div class="map" role="img" aria-label="Street map showing the shop location"></div>
    <div class="address">42 Elmwood Ave Fairhaven, CT 06500</div>
    <div class="call">
      <span class="call-label">CALL US</span>
      <svg viewBox="0 0 24 24"><path d="M6.6 10.8a15.1 15.1 0 0 0 6.6 6.6l2.2-2.2a1 1 0 0 1 1-.25 11.4 11.4 0 0 0 3.6.57 1 1 0 0 1 1 1V20a1 1 0 0 1-1 1A17 17 0 0 1 3 4a1 1 0 0 1 1-1h3.5a1 1 0 0 1 1 1c0 1.25.2 2.45.57 3.6a1 1 0 0 1-.25 1z"/></svg>
      <span class="call-number">(203) 555-0148</span>
    </div>
    <div class="contact-row">
      <span><svg viewBox="0 0 20 20"><rect x="2" y="4" width="16" height="12"/><path d="M2 4l8 7 8-7"/></svg>hello@harborlinewine.com</span>
      <span><svg viewBox="0 0 20 20"><circle cx="10" cy="10" r="8"/><ellipse cx="10" cy="10" rx="3.5" ry="8"/><path d="M2 10h16"/></svg>www.harborlinewine.com</span>
    </div>
    <div class="brand"><span class="brand-dot"></span><span class="brand-name">HARBORLINE<br>WINE &amp; SPIRITS</span></div>
    <div class="stamp"></div>
    <div class="accept">
      <span class="accept-label">WE<br>ACCEPT</span>
      <span class="pay">QuickPay</span><span class="pay">TapPay</span><span class="pay">WalletPay</span>
    </div>
  </section>
</div>

<div class="preview preview-front">
  <section class="card front">
    <svg class="shapes" viewBox="0 0 972 648" aria-hidden="true">
      <circle cx="790" cy="205" r="320" fill="var(--gold)"/>
      <path fill="var(--gold)" d="M405 648C430 585 480 560 560 560H640C690 560 700 490 760 490H972V648Z"/>
      <circle cx="0" cy="648" r="92" fill="var(--gold)"/>
      <circle cx="0" cy="648" r="104" fill="none" stroke="var(--gold)" stroke-width="4" stroke-dasharray="2 7" stroke-linecap="round"/>
    </svg>
    <div class="photo photo-bottles" role="img" aria-label="Photo of rye whiskey, wine bottles and stout cans on a counter"></div>
    <div class="photo photo-storefront" role="img" aria-label="Photo of the shop storefront"></div>
    <div class="brand"><span class="brand-dot"></span><span class="brand-name">HARBORLINE<br>WINE &amp; SPIRITS</span></div>
    <div class="kicker">NOW IN YOUR NEIGHBORHOOD</div>
    <div class="headline">Harborline Wine &amp; Spirits</div>
    <div class="subtitle">High End Wine &amp; Spirits Shop</div>
    <div class="service-bar bar-1">WINE, BEER &amp; SPIRITS STORE ·</div>
    <div class="service-bar bar-2">WINE/SPIRITS · TOBACCO STORE</div>
    <p class="intro">Harborline Wine &amp; Spirits, your local package store to satisfy all of your tastes without breaking the bank or making it complex.</p>
    <div class="address"><svg viewBox="0 0 20 28"><path d="M10 0a10 10 0 0 0-10 10c0 7.5 10 18 10 18s10-10.5 10-18A10 10 0 0 0 10 0zm0 14a4 4 0 1 1 0-8 4 4 0 0 1 0 8z"/></svg>42 Elmwood Ave Fairhaven, CT 06500</div>
    <div class="web">www.harborlinewine.com</div>
    <div class="perks">
      <div class="perk-row">Free Wi-Fi available</div>
      <div class="perk-row"><svg viewBox="0 0 36 30"><rect x="12" y="2" width="22" height="20"/><path d="M2 12h9v10H2z"/><circle cx="8" cy="25" r="4"/><circle cx="27" cy="25" r="4"/></svg>Offers home delivery</div>
    </div>
  </section>
</div>

<!-- ===== Front, full size ===== -->
<div class="sheet-front">
  <section class="card front">
    <svg class="shapes" viewBox="0 0 972 648" aria-hidden="true">
      <circle cx="790" cy="205" r="320" fill="var(--gold)"/>
      <path fill="var(--gold)" d="M405 648C430 585 480 560 560 560H640C690 560 700 490 760 490H972V648Z"/>
      <circle cx="0" cy="648" r="92" fill="var(--gold)"/>
      <circle cx="0" cy="648" r="104" fill="none" stroke="var(--gold)" stroke-width="4" stroke-dasharray="2 7" stroke-linecap="round"/>
    </svg>
    <div class="photo photo-bottles" role="img" aria-label="Photo of rye whiskey, wine bottles and stout cans on a counter"></div>
    <div class="photo photo-storefront" role="img" aria-label="Photo of the shop storefront"></div>
    <div class="brand"><span class="brand-dot"></span><span class="brand-name">HARBORLINE<br>WINE &amp; SPIRITS</span></div>
    <div class="kicker">NOW IN YOUR NEIGHBORHOOD</div>
    <div class="headline">Harborline Wine &amp; Spirits</div>
    <div class="subtitle">High End Wine &amp; Spirits Shop</div>
    <div class="service-bar bar-1">WINE, BEER &amp; SPIRITS STORE ·</div>
    <div class="service-bar bar-2">WINE/SPIRITS · TOBACCO STORE</div>
    <p class="intro">Harborline Wine &amp; Spirits, your local package store to satisfy all of your tastes without breaking the bank or making it complex.</p>
    <div class="address"><svg viewBox="0 0 20 28"><path d="M10 0a10 10 0 0 0-10 10c0 7.5 10 18 10 18s10-10.5 10-18A10 10 0 0 0 10 0zm0 14a4 4 0 1 1 0-8 4 4 0 0 1 0 8z"/></svg>42 Elmwood Ave Fairhaven, CT 06500</div>
    <div class="web">www.harborlinewine.com</div>
    <div class="perks">
      <div class="perk-row">Free Wi-Fi available</div>
      <div class="perk-row"><svg viewBox="0 0 36 30"><rect x="12" y="2" width="22" height="20"/><path d="M2 12h9v10H2z"/><circle cx="8" cy="25" r="4"/><circle cx="27" cy="25" r="4"/></svg>Offers home delivery</div>
    </div>
  </section>
</div>

<!-- ===== Back, full size ===== -->
<div class="sheet-back">
  <section class="card back">
    <svg class="shapes" viewBox="0 0 972 648" aria-hidden="true">
      <path fill="var(--gold)" d="M0 0H455C515 20 548 95 543 165C538 245 485 290 480 350C476 430 560 480 610 555C632 590 645 620 652 648H0Z"/>
      <path fill="var(--ink)" d="M0 109H480C515 150 522 205 510 250C498 295 470 318 445 335H0Z"/>
    </svg>
    <div class="headline">Harborline Wine &amp; Spirits</div>
    <div class="subtitle">High End Wine &amp; Spirits Shop</div>
    <div class="review">
      <span class="stars">★★★★★</span>
      <span class="quote-mark quote-open">“</span>
      <p class="review-text">Great neighborhood liquor store. Very neat, very clean, and modern looking. The owner is very accommodating and if she doesn't have something, she's willing to try and get it for you. Prices seem to be on par with other stores in the area.<br>I'd rather shop here and support a small business instead of one of the super-mega booze stores.</p>
      <span class="quote-mark quote-close">”</span>
      <p class="reviewer">Dana R.<br>Fairhaven, CT</p>
    </div>
    <div class="hours"><div class="hours-open">OPEN ON</div><div class="hours-days">MONDAY TO SUNDAY</div></div>
    <div class="photo photo-shelf" role="img" aria-label="Photo of bottles lined up on a store shelf"></div>
    <div class="photo photo-display" role="img" aria-label="Photo of a chilled bottle display in the store"></div>
    <div class="map" role="img" aria-label="Street map showing the shop location"></div>
    <div class="address">42 Elmwood Ave Fairhaven, CT 06500</div>
    <div class="call">
      <span class="call-label">CALL US</span>
      <svg viewBox="0 0 24 24"><path d="M6.6 10.8a15.1 15.1 0 0 0 6.6 6.6l2.2-2.2a1 1 0 0 1 1-.25 11.4 11.4 0 0 0 3.6.57 1 1 0 0 1 1 1V20a1 1 0 0 1-1 1A17 17 0 0 1 3 4a1 1 0 0 1 1-1h3.5a1 1 0 0 1 1 1c0 1.25.2 2.45.57 3.6a1 1 0 0 1-.25 1z"/></svg>
      <span class="call-number">(203) 555-0148</span>
    </div>
    <div class="contact-row">
      <span><svg viewBox="0 0 20 20"><rect x="2" y="4" width="16" height="12"/><path d="M2 4l8 7 8-7"/></svg>hello@harborlinewine.com</span>
      <span><svg viewBox="0 0 20 20"><circle cx="10" cy="10" r="8"/><ellipse cx="10" cy="10" rx="3.5" ry="8"/><path d="M2 10h16"/></svg>www.harborlinewine.com</span>
    </div>
    <div class="brand"><span class="brand-dot"></span><span class="brand-name">HARBORLINE<br>WINE &amp; SPIRITS</span></div>
    <div class="stamp"></div>
    <div class="accept">
      <span class="accept-label">WE<br>ACCEPT</span>
      <span class="pay">QuickPay</span><span class="pay">TapPay</span><span class="pay">WalletPay</span>
    </div>
  </section>
</div>

</body>
</html>
```